Webpage for a treatment housing for young addicts.

I need a new design and files for my wordpress page. I need it to be more neat and clean. I need it to look professional with a starting page that will work as a navigation. I need like logo and phone number and such up top, a picture under it with one sentence as a slogan and under it 6 boxes to click to come to our different pages. Under it I want news etc.

Target Market(s)

Social services, employees and governements

Coding

Coded - Design and coding required

Font styles to use
Sans Serif

Colors
abd037
3176b5
9d9d9d
aaaaaa
f04a50

Requirements
Must have
• A nice design
Nice to have
• need it to look professional with a starting page that will work as a navigation. I need like logo and phone number and such up top, a picture under it with one sentence as a slogan and under it 6 boxes to click to come to our different pages. Under it I want news etc.
• today www.kolrev.se
• want more like www.tralvik.se or www.bersona.se
Should not have
• To many different colours and a messy design.

```html
<!DOCTYPE html>
<html lang="en">
<head>
<meta charset="utf-8">
<title>7KR Omsorg AB – Care and housing</title>
<link href="https://fonts.googleapis.com/css2?family=Archivo+Black&family=Lato:wght@400;700;900&display=swap" rel="stylesheet">
<style>
:root{
  --lime:#abd037;
  --blue:#3176b5;
  --blue-dark:#2a5f94;
  --grey:#9d9d9d;
  --grey-2:#aaaaaa;
  --ink:#2b2b2b;
  --text:#6a6a6a;
  --band:#f0f0f0;
  --band-2:#ececec;
  --white:#ffffff;
}
*{box-sizing:border-box;margin:0;padding:0}
html,body{width:1200px;height:4176px;overflow:hidden}
body{position:relative;background:var(--white);font-family:"Lato",Arial,sans-serif;color:var(--text)}
.abs{position:absolute}
.heading{font-family:"Archivo Black","Arial Black",sans-serif;color:var(--blue);text-transform:uppercase;letter-spacing:1px;font-weight:400}
.btn{position:absolute;display:flex;align-items:center;justify-content:center;color:#fff;font-size:20px;text-transform:uppercase;background:linear-gradient(#5b7c8a,#3f5965);border-radius:2px}

/* top bar */
.topbar{left:0;top:0;width:1200px;height:42px;border-bottom:1px solid #e2e2e2;font-size:15px}
.topbar .hours{left:80px;top:11px;display:flex;gap:8px;align-items:center;color:var(--lime)}
.topbar .phone{left:750px;top:11px;display:flex;gap:8px;align-items:center;color:var(--ink)}
.topbar .search{left:912px;top:8px;width:90px;height:26px;border-left:1px solid #ddd;padding-left:12px;color:var(--grey-2);font-size:14px;line-height:26px}
.topbar .social{left:1002px;top:0;display:flex}
.topbar .social span{width:38px;height:42px;border-left:1px solid #e2e2e2;display:flex;align-items:center;justify-content:center}
.topbar .social i{width:12px;height:12px;background:var(--blue-dark)}
.topbar .social span:nth-child(2) i{background:var(--lime)}

/* header */
.logo{left:80px;top:56px;display:flex;align-items:center;gap:12px}
.logo .mark{width:56px;height:56px;background:var(--lime)}
.logo .name{font-weight:900;font-size:38px;color:var(--blue);letter-spacing:1px}
.nav{left:506px;top:86px;display:flex;gap:46px;font-size:14px;text-transform:uppercase;color:#777}

/* hero */
.hero{left:0;top:158px;width:1200px;height:520px;background:linear-gradient(160deg,#6b5a3e 0%,#8a6e4e 25%,#5e7a3a 55%,#7f9b45 75%,#4b6331 100%)}
.slogan{left:78px;top:348px;width:626px;height:131px;background:var(--lime);padding:20px 0 0 32px;font-family:"Archivo Black","Arial Black",sans-serif;font-size:40px;line-height:46px;box-shadow:0 4px 10px rgba(0,0,0,.25)}
.slogan .l1{color:var(--white)}
.slogan .l2{color:#111}

/* quick links */
.quick-band{left:0;top:678px;width:1200px;height:232px;background:var(--band)}
.quick{width:343px;height:52px;color:#fff;font-size:18px;line-height:19px;display:flex;align-items:center;padding:0 50px 0 18px}
.quick svg{position:absolute;right:16px;top:18px}
.q-grey{background:var(--grey)} .q-blue{background:var(--blue)} .q-lime{background:var(--lime)}

/* work */
.work-title{left:0;width:1200px;top:966px;text-align:center;font-size:46px}
.work-text{left:0;width:1200px;top:1046px;text-align:center;font-size:16px;line-height:24px;color:var(--grey)}

/* about */
.about-frame{left:159px;top:1222px;width:924px;height:485px;border:1px solid #dcdcdc;box-shadow:0 2px 6px rgba(0,0,0,.08)}
.about-photo{left:78px;top:1314px;width:473px;height:301px;background:linear-gradient(135deg,#8b4a3a,#b47a5e 50%,#6d5547);box-shadow:0 4px 10px rgba(0,0,0,.3)}
.about-title{left:618px;top:1312px;font-size:44px}
.about-text{left:620px;top:1372px;width:430px;font-size:15px;line-height:22px}

/* feature cards */
.feature-band{left:0;top:1771px;width:1200px;height:428px;background:var(--band-2)}
.card{top:1832px;width:332px;height:303px}
.card .pic{height:192px}
.card .cap{height:111px;padding:22px 50px 0 22px;color:#111;font-weight:900;font-size:19px;line-height:23px;position:relative}
.card .cap svg{position:absolute;right:20px;bottom:20px}

/* newsletter */
.letter{left:245px;top:2277px;width:715px;height:265px;border:1px solid #ddd;border-top:6px solid var(--lime);background:#fff}
.letter .edge{position:absolute;right:-14px;top:-6px;width:14px;height:calc(100% + 6px);background:#e6e6e6}
.letter-text{left:320px;top:2378px;width:560px;text-align:center;font-size:14px;line-height:20px;color:var(--grey)}
.email{left:340px;top:2444px;width:342px;height:42px;border:1px solid #d6d6d6;font-size:14px;padding:0 12px;line-height:40px;color:#999}

/* news */
.news-band{left:0;top:2547px;width:1200px;height:404px;background:var(--band)}
.news-title{left:0;width:1200px;top:2604px;text-align:center;font-size:44px}
.news-pic{top:2681px;width:234px;height:209px}
.news-body{top:2676px;width:250px}
.news-body h3{font-family:"Archivo Black","Arial Black",sans-serif;color:#111;font-size:19px;line-height:24px;font-weight:400}
.news-body .date{margin-top:14px;padding:10px 0;border-top:1px solid #ddd;border-bottom:1px solid #ddd;font-size:14px;color:#999;display:flex;gap:10px;align-items:center}
.news-body p{margin-top:14px;font-size:14px;line-height:21px}
.news-body .more{margin-top:24px;font-weight:900;font-size:15px;color:#111;text-decoration:underline}

/* social */
.social-title{left:0;width:1200px;top:3006px;text-align:center;font-size:44px}
.social-panel{left:78px;top:3082px;width:1044px;height:334px;background:var(--band)}
.fb{left:100px;top:3100px;width:300px;height:300px;font-size:12px}
.fb .head{display:flex;gap:10px;align-items:center}
.fb .head i{width:44px;height:44px;background:var(--lime)}
.fb .head b{font-size:22px;color:#222;font-weight:900}
.fb .cover{margin-top:22px;height:80px;border:1px solid #ddd;background:#fff;display:flex;align-items:center;justify-content:center;font-weight:900;font-size:30px;color:var(--blue)}
.fb .post{margin-top:28px;display:flex;gap:10px;font-size:14px;color:#333;line-height:18px}
.fb .post i{flex:none;width:38px;height:38px;border-radius:50%;background:#b7a58f}
.video{left:426px;top:3082px;width:348px;height:334px;background:linear-gradient(#3c4656,#2a303b);text-align:center;color:#fff}
.video .follow{margin-top:116px;font-weight:900;font-size:22px}
.video .sq{width:50px;height:50px;background:#fff;margin:14px auto 0}
.video .tag{margin-top:30px;font-weight:900;font-size:40px}
.shot{left:806px;top:3100px;width:300px;height:300px}

/* ideas */
.ideas{left:0;top:3480px;width:1200px;height:440px;background:linear-gradient(90deg,#2a5fb0 0%,#3a86cc 45%,#5fb6c0 70%,var(--lime) 100%)}
.ideas-title{left:78px;top:3530px;font-family:"Archivo Black","Arial Black",sans-serif;font-size:42px;line-height:48px;color:#fff;font-weight:400}
.ideas-text{left:78px;top:3692px;width:500px;font-size:15px;line-height:23px;color:#fff}
.ideas-pic{left:649px;top:3550px;width:473px;height:306px;background:linear-gradient(135deg,#3d3128,#6f5a44 50%,#a36a3c);box-shadow:0 4px 12px rgba(0,0,0,.35)}
.btn-light{background:linear-gradient(#f4f4f4,#cfcfcf);color:#3a5a6a}

/* footer */
.footer{left:0;top:3920px;width:1200px;height:256px;background:#f7f7f7}
.contact{top:3970px;display:flex;gap:14px;align-items:center;font-size:14px;color:#555;line-height:19px}
.foot-nav{left:0;width:1200px;top:4074px;display:flex;justify-content:center;gap:26px;font-size:14px;color:#888}
.foot-nav .on{color:#222;text-decoration:underline}
.foot-rule{left:300px;top:4114px;width:600px;height:1px;background:#ddd}
.copy{left:0;width:1200px;top:4134px;text-align:center;font-size:13px;color:#888}
.copy b{color:var(--blue)}
</style>
</head>
<body>

<!-- top bar -->
<div class="abs topbar">
  <div class="abs hours">
    <svg width="20" height="20" viewBox="0 0 20 20"><circle cx="10" cy="10" r="8.5" fill="none" stroke="#3176b5" stroke-width="2"/><path d="M10 5v5l3 2" stroke="#3176b5" stroke-width="2" fill="none"/></svg>
    Monday - Friday : 9:00 - 18:00
  </div>
  <div class="abs phone">
    <svg width="18" height="18" viewBox="0 0 24 24"><path d="M6.6 10.8a15 15 0 006.6 6.6l2.2-2.2c.3-.3.7-.4 1-.2 1.1.4 2.3.6 3.6.6.6 0 1 .4 1 1V20c0 .6-.4 1-1 1A17 17 0 013 4c0-.6.4-1 1-1h3.5c.6 0 1 .4 1 1 0 1.3.2 2.5.6 3.6.1.3 0 .7-.2 1z" fill="#3176b5"/></svg>
    010-4408210
  </div>
  <div class="abs search">Search</div>
  <div class="abs social"><span><i></i></span><span><i></i></span><span><i></i></span></div>
</div>

<!-- header -->
<div class="abs logo"><div class="mark"></div><div class="name">7KR</div></div>
<nav class="abs nav"><span>Home</span><span>About 7KR</span><span>Ekbacken HVB</span><span>Work with us</span><span>Plug</span></nav>

<!-- hero -->
<div class="abs hero" role="img" aria-label="Photo of a garden with a lawn, flowering shrubs and a wooden house with a tiled roof"></div>
<div class="abs slogan"><div class="l1">We Create Sustainable</div><div class="l2">Roads to a Better Future</div></div>

<!-- quick links -->
<div class="abs quick-band"></div>
<div class="abs quick q-grey" style="left:78px;top:738px">Therapeutic Environment The<svg width="18" height="16" viewBox="0 0 18 16"><path d="M2 2l6 6-6 6M9 2l6 6-6 6" stroke="#fff" stroke-width="2" fill="none"/></svg></div>
<div class="abs quick q-blue" style="left:429px;top:738px">The starting point of the treatment<svg width="18" height="16" viewBox="0 0 18 16"><path d="M2 2l6 6-6 6M9 2l6 6-6 6" stroke="#fff" stroke-width="2" fill="none"/></svg></div>
<div class="abs quick q-lime" style="left:777px;top:738px">Individually tailored<svg width="18" height="16" viewBox="0 0 18 16"><path d="M2 2l6 6-6 6M9 2l6 6-6 6" stroke="#fff" stroke-width="2" fill="none"/></svg></div>
<div class="abs quick q-blue" style="left:78px;top:798px">Influence and self-determination over healthcare<svg width="18" height="16" viewBox="0 0 18 16"><path d="M2 2l6 6-6 6M9 2l6 6-6 6" stroke="#fff" stroke-width="2" fill="none"/></svg></div>
<div class="abs quick q-lime" style="left:429px;top:798px">Active contact person<svg width="18" height="16" viewBox="0 0 18 16"><path d="M2 2l6 6-6 6M9 2l6 6-6 6" stroke="#fff" stroke-width="2" fill="none"/></svg></div>
<div class="abs quick q-blue" style="left:777px;top:798px">BVIS<svg width="18" height="16" viewBox="0 0 18 16"><path d="M2 2l6 6-6 6M9 2l6 6-6 6" stroke="#fff" stroke-width="2" fill="none"/></svg></div>

<!-- work -->
<h2 class="abs heading work-title">Work at 7KR</h2>
<p class="abs work-text">Looking forward to becoming part of a business in progress with the vision of being the best?<br>Then you may want to look at our company.</p>
<div class="btn" style="left:510px;top:1111px;width:178px;height:47px">Search job</div>

<!-- about -->
<div class="abs about-frame"></div>
<div class="abs about-photo" role="img" aria-label="Photo of a group of young people standing on outdoor steps"></div>
<h2 class="abs heading about-title">About us</h2>
<p class="abs about-text">7KR Omsorg AB carries out care and care aimed at people aged 14-25 years. This is done primarily through Home for care and housing (HVB). We are specialists in psychosocial abuse and crime issues. By being constantly open to new methods and aware of the existing ones, we develop and improve our care. The methods are adapted to the individual, we do not think that ONE thought or ONE perspective can be applied to everyone.</p>
<div class="btn" style="left:618px;top:1559px;width:175px;height:50px">Learn more</div>

<!-- feature cards -->
<div class="abs feature-band"></div>
<div class="abs card" style="left:78px">
  <div class="pic" role="img" aria-label="Photo of two women talking" style="background:linear-gradient(135deg,#d8cdb8,#a89478)"></div>
  <div class="cap" style="background:var(--blue)">The Assistant pads are here!<svg width="24" height="24" viewBox="0 0 24 24"><circle cx="12" cy="12" r="11" fill="#111"/><path d="M7 12h9M12 8l4 4-4 4" stroke="#fff" stroke-width="2" fill="none"/></svg></div>
</div>
<div class="abs card" style="left:434px">
  <div class="pic" role="img" aria-label="Photo of warm city lights at night with the word Culture" style="background:linear-gradient(135deg,#3a2418,#b5652a 55%,#5a3320)"></div>
  <div class="cap" style="background:var(--lime)">Inclusive culture<svg width="24" height="24" viewBox="0 0 24 24"><circle cx="12" cy="12" r="11" fill="#111"/><path d="M7 12h9M12 8l4 4-4 4" stroke="#fff" stroke-width="2" fill="none"/></svg></div>
</div>
<div class="abs card" style="left:791px">
  <div class="pic" role="img" aria-label="Photo of a young person with a backpack outside a house" style="background:linear-gradient(135deg,#8c8c86,#c9c4b6 50%,#6f6a60)"></div>
  <div class="cap" style="background:var(--blue)">Sweden needs more family homes<svg width="24" height="24" viewBox="0 0 24 24"><circle cx="12" cy="12" r="11" fill="#111"/><path d="M7 12h9M12 8l4 4-4 4" stroke="#fff" stroke-width="2" fill="none"/></svg></div>
</div>

<!-- newsletter -->
<div class="abs letter"><div class="edge"></div></div>
<p class="abs letter-text">Subscribe now and receive weekly newsletter with work in different parts for caring home, such as finance, personnel, marketing, customer contacts and much more!</p>
<div class="abs email">Email</div>
<div class="btn" style="left:682px;top:2444px;width:178px;height:42px;background:linear-gradient(#3d8a7c,#2c6a60)">Subscribe</div>

<!-- news -->
<div class="abs news-band"></div>
<h2 class="abs heading news-title">Latest news</h2>
<div class="abs news-pic" style="left:78px;background:linear-gradient(135deg,#e9e4da,#b9ad97 60%,#7d7262)" role="img" aria-label="Photo of a bright modern kitchen"></div>
<div class="abs news-body" style="left:323px">
  <h3>Lorem Ipsum is simply dummy text.</h3>
  <div class="date"><svg width="16" height="16" viewBox="0 0 16 16"><rect x="1" y="3" width="14" height="12" fill="none" stroke="#aaa" stroke-width="1.5"/><path d="M1 7h14M5 1v4M11 1v4" stroke="#aaa" stroke-width="1.5"/></svg>20 Dec,2018</div>
  <p>Lorem Ipsum is simply dummy text of the printing and typesetting.</p>
  <div class="more">READ MORE »</div>
</div>
<div class="abs news-pic" style="left:607px;background:linear-gradient(160deg,#8fb24f,#4f7a2c 50%,#9c3b2f 75%,#3f6a25)" role="img" aria-label="Photo of a red wooden house among green trees"></div>
<div class="abs news-body" style="left:852px">
  <h3>Lorem Ipsum is simply dummy text.</h3>
  <div class="date"><svg width="16" height="16" viewBox="0 0 16 16"><rect x="1" y="3" width="14" height="12" fill="none" stroke="#aaa" stroke-width="1.5"/><path d="M1 7h14M5 1v4M11 1v4" stroke="#aaa" stroke-width="1.5"/></svg>10 Dec,2018</div>
  <p>Lorem Ipsum is simply dummy text of the printing and typesetting.</p>
  <div class="more">READ MORE »</div>
</div>

<!-- social -->
<h2 class="abs heading social-title">Social media</h2>
<div class="abs social-panel"></div>
<div class="abs fb">
  <div class="head"><i></i><div><b>7KR Omsorg AB</b><br>340 likes</div></div>
  <div class="cover">7KR</div>
  <div class="post"><i></i><div>A new week with new plans, join our team today!<br><span style="color:#999;font-size:12px">5 days ago at 11:04</span></div></div>
</div>
<div class="abs video">
  <div class="follow">Follow Us on</div>
  <div class="sq"></div>
  <div class="tag">#7kr</div>
</div>
<div class="abs shot" role="img" aria-label="Screenshot of a social page post with a small photo and text" style="background:linear-gradient(#ffffff,#dfe6ee 40%,#ffffff)"></div>

<!-- ideas -->
<div class="abs ideas"></div>
<h2 class="abs ideas-title">OUR IDEAS ABOUT<br>WORKING METHODS<br>&amp; TREATMENT!</h2>
<p class="abs ideas-text">We want to create a therapeutic treatment environment through evidence-based methods, high skills and combined experience. We want every individual to have the opportunity to change and influence his own situation for a better and more well functioning.</p>
<div class="btn btn-light" style="left:78px;top:3808px;width:178px;height:48px">Learn more</div>
<div class="abs ideas-pic" role="img" aria-label="Photo of hands planting a seedling in a clay pot"></div>

<!-- footer -->
<div class="abs footer"></div>
<div class="abs contact" style="left:190px">
  <svg width="18" height="24" viewBox="0 0 18 24"><path d="M9 1a8 8 0 00-8 8c0 6 8 14 8 14s8-8 8-14a8 8 0 00-8-8z" fill="#3176b5"/><circle cx="9" cy="9" r="3" fill="#fff"/></svg>
  <div>7KR Omsorg AB<br>Lindvägen 22<br>123 45 Tallby</div>
</div>
<div class="abs contact" style="left:556px;top:3990px">
  <svg width="18" height="18" viewBox="0 0 24 24"><path d="M6.6 10.8a15 15 0 006.6 6.6l2.2-2.2c.3-.3.7-.4 1-.2 1.1.4 2.3.6 3.6.6.6 0 1 .4 1 1V20c0 .6-.4 1-1 1A17 17 0 013 4c0-.6.4-1 1-1h3.5c.6 0 1 .4 1 1 0 1.3.2 2.5.6 3.6.1.3 0 .7-.2 1z" fill="#3176b5"/></svg>
  010-4408210
</div>
<div class="abs contact" style="left:778px;top:3990px">
  <svg width="20" height="16" viewBox="0 0 20 16"><rect x="1" y="1" width="18" height="14" fill="#3176b5"/><path d="M1 1l9 7 9-7" stroke="#fff" stroke-width="1.5" fill="none"/></svg>
  info@7kromsorg.se
</div>
<nav class="abs foot-nav"><span class="on">Home</span><span>About 7KR</span><span>Ekbacken HVB</span><span>Work with us</span><span>Contact Us</span></nav>
<div class="abs foot-rule"></div>
<p class="abs copy">© <b>7KR Omsorg AB</b> 2018 &nbsp;|&nbsp; Privacy Policy</p>

</body>
</html>
```